Re-design of current business cards

We are updating our website with new colors and layout. Would like to re-design our business cards to co-ordinate. See attached pdf with new Brightwell website colors. We would also like to combine our 2 brands on the one business card. Attached is the new design for our Brightwell website, current business cards, which are one sided, brightwell logo in tiff, .ai for fonts. Brightwell logo font is Optimum, Lanterncove website home page image, Lanterncove brand statics for products which includes the logo for this brand.

Lanterncove brand will stay the dark gray on the website. See attached statics for product and website home page.
Updates

The business cards will be 2 sided. Brightwell Brand on one side and Lanterncove Brand on the other. The colors for Brightwell need to follow the color scheme of the brightwell website pdf I uploaded. The colors are a blue, lighter teal blue and white. Lanterncove needs to follow the dark gray color on files uploaded

Target Market(s)

The trade and consumers

Industry/Entity Type

Home Furnishing

Contact Information for Business Card

We are updating our website with new colors and layout. Would like to re-design our business cards to co-ordinate. We would also like to combine our 2 brands onto 1 2 sided business cards.

Requirements
Must have
• Colors that match our new website, see attached image.
• RGB colors
• navy -#152842
• teal - 98aeb9
• The gray color used for Lanterncove brands.
• ll logos and fonts should stay the same.

```html
<!DOCTYPE html>
<html lang="en">
<head>
<meta charset="utf-8">
<title>Brightwell &amp; Lanterncove Business Card</title>
<link rel="stylesheet" href="https://fonts.googleapis.com/css2?family=Cormorant+Garamond:wght@500&family=Marcellus&family=Arimo:wght@400&display=swap">
<style>
  :root {
    --backdrop: #e9e7e3;
    --card-gray: #5a5b5d;
    --card-white: #f6f6f4;
    --ink-light: #eeeeee;
    --ink-soft: #d4d4d4;
    --brand-navy: #152842;
    --brand-teal: #98aeb9;
    --teal-deep: #7f98a5;
  }
  * { box-sizing: border-box; margin: 0; padding: 0; }
  html, body { width: 1200px; height: 886px; overflow: hidden; }
  body { background: var(--backdrop); position: relative; font-family: "Arimo", Arial, sans-serif; }

  .card {
    position: absolute;
    width: 520px;
    height: 297px;
    box-shadow: 0 6px 18px rgba(0,0,0,0.18);
  }

  /* Lanterncove side */
  .card--lanterncove { left: 80px; top: 140px; background: var(--card-gray); color: var(--ink-light); text-align: center; }
  .lc-wordmark { position: absolute; left: 0; right: 0; top: 74px; }
  .lc-name { font-family: "Cormorant Garamond", Georgia, serif; font-weight: 500; font-size: 50px; letter-spacing: 1px; line-height: 1; }
  .lc-byline { font-family: "Cormorant Garamond", Georgia, serif; font-size: 9px; letter-spacing: 1px; margin-top: 2px; padding-left: 250px; }
  .lc-tagline { position: absolute; left: 0; right: 0; top: 158px; font-size: 17px; color: var(--ink-soft); letter-spacing: 0.3px; }
  .lc-details { position: absolute; left: 0; right: 0; top: 206px; font-size: 12.5px; line-height: 1.45; color: var(--ink-light); }

  /* Brightwell side */
  .card--brightwell { left: 600px; top: 450px; background: var(--card-white); color: var(--brand-navy); overflow: hidden; }
  .bw-name { position: absolute; left: 30px; top: 26px; font-family: "Marcellus", Georgia, serif; font-size: 34px; letter-spacing: 1px; color: var(--brand-navy); }
  .bw-emblem {
    position: absolute; left: 300px; top: 70px; width: 200px; height: 205px;
    background: linear-gradient(160deg, var(--brand-teal), var(--teal-deep));
  }
  .person { position: absolute; left: 30px; top: 78px; }
  .person-name { font-family: "Marcellus", Georgia, serif; font-size: 19px; letter-spacing: 0.8px; color: var(--teal-deep); }
  .person-role { font-size: 13px; line-height: 1.3; color: var(--brand-navy); margin-top: 2px; }
  .address { position: absolute; left: 30px; top: 150px; font-size: 13px; line-height: 1.35; }
  .contacts { position: absolute; left: 30px; top: 190px; list-style: none; font-size: 13px; line-height: 1.35; }
  .contacts li { display: flex; align-items: center; gap: 7px; }
  .contacts svg { width: 10px; height: 10px; fill: var(--brand-teal); flex: none; }
  .contacts .plain { padding-left: 17px; }
</style>
</head>
<body>
  <section class="card card--lanterncove" aria-label="Lanterncove side">
    <div class="lc-wordmark">
      <div class="lc-name">LANTERNCOVE</div>
      <div class="lc-byline">by BRIGHTWELL</div>
    </div>
    <p class="lc-tagline">Discover the luxury of home.</p>
    <p class="lc-details">Exclusive Designs | Limited Distribution | Generous Proportion<br>Limited Introduction October 2015 Full Collection Launch April 2016</p>
  </section>

  <section class="card card--brightwell" aria-label="Brightwell side">
    <div class="bw-name">BRIGHTWELL</div>
    <div class="bw-emblem" role="img" aria-label="Large world map illustration"></div>
    <div class="person">
      <div class="person-name">DANA WHITFIELD</div>
      <div class="person-role">Graphics<br>Photography Director</div>
    </div>
    <p class="address">PoBox 412/1870 Alder Ridge Rd<br>Maple Falls, Virginia 24000</p>
    <ul class="contacts">
      <li><svg viewBox="0 0 10 10" aria-label="Phone"><path d="M2 0.5 L3.6 2.6 L2.8 3.6 Q4 6 6.4 7.2 L7.4 6.4 L9.5 8 L8.4 9.5 Q2.5 8.8 0.5 1.6 Z"/></svg>555.204.7310</li>
      <li><svg viewBox="0 0 10 10" aria-label="Fax"><rect x="2.5" y="0.5" width="5" height="3"/><rect x="0.5" y="4" width="9" height="4.5" rx="1"/></svg>555.204.7388</li>
      <li><svg viewBox="0 0 10 10" aria-label="Email"><rect x="0.5" y="1.5" width="9" height="7"/><path d="M0.5 1.5 L5 5.5 L9.5 1.5" fill="none" stroke="#f6f6f4" stroke-width="1"/></svg>dwhitfield@brightwell.com</li>
      <li><svg viewBox="0 0 10 10" aria-label="Website"><circle cx="5" cy="5" r="4.5"/></svg>www.brightwell.com</li>
      <li class="plain">www.brightwell.com</li>
    </ul>
  </section>
</body>
</html>
```